Need UI Design for HRIS/Company Employee Portal

Currently have a custom built system that we hire and use as our employee database and employee portal for everyone in our company. The software has evolved dramatically and needs to be completely user friendly and aesthetically pleasing. Attached are a few ideas and pages we already have. Please make 5 designs for the 5 different pages below. Would need all specifications of content used, color code, font/typography, icons used, etc. We can pretty much pull any information from anywhere we have for example, employee photo, address, DOB, Hire date, Title, ETC.

-Company Staff/Admin Welcome Page
- We want quick shortcuts/buttons or icons for staff functions, such as terminate, hire, information change, reports, etc
-Employee Profile Welcome Page
- We want quick shortcuts/buttons or icons for direct deposit, time off request, information change, pay stubs
-List of Applications/Candidates Page
-Profile Search Page
-Manage Inventory

Target Market(s)

Employees

Industry/Entity Type

It Company

Coding

Coded - Design and coding required

Number of Pages Required

5+ page

Font styles to use
Sans Serif

Requirements
Must have
• Must be professional! Aesthetics, Icons, Easy User Interface, Modern New technology look, can be responsive to mobile
Should not have
• Nothing old school

```html
<!DOCTYPE html>
<html lang="en">
<head>
<meta charset="utf-8">
<title>Employee Portal – Profile</title>
<link rel="stylesheet" href="https://fonts.googleapis.com/css2?family=Barlow:wght@400;500;600&display=swap">
<style>
:root{
  --white:#ffffff;
  --nav:#0a78dc;
  --btn:#0a78dc;
  --accent:#4f9fe6;
  --yellow:#f3c614;
  --card-dark:rgba(38,22,70,.82);
  --card-navy:rgba(25,28,78,.9);
  --muted:#c9cde6;
  --ink:#333a44;
  --grey:#8a8f99;
  --green:#7cb342;
}
*{box-sizing:border-box;margin:0;padding:0}
html,body{width:1200px;height:1114px;overflow:hidden}
body{font-family:"Barlow",sans-serif;color:var(--white);position:relative;
  background:linear-gradient(120deg,#e8000a 0%,#b4163a 14%,#5a2a8a 30%,#2241c4 48%,#1d36a8 62%,#1c1a55 80%,#1a1444 100%);}
.abs{position:absolute}
.header{left:0;top:0;width:1200px;height:88px;background:var(--white)}
.brand{left:200px;top:30px;display:flex;align-items:center;gap:10px}
.brand-mark{width:28px;height:28px;border-radius:50%;background:#1e3d9c}
.brand-name{font-size:13px;font-weight:600;color:#1e3d9c;letter-spacing:.3px}
.nav{left:0;top:88px;width:1200px;height:50px;background:var(--nav);display:flex;align-items:center;padding-left:210px;gap:32px;font-size:12.5px;font-weight:500;letter-spacing:.3px}
.card{position:absolute}
.profile{left:201px;top:178px;width:252px;height:393px;background:var(--card-dark);text-align:center}
.photo{position:absolute;left:48px;top:26px;width:157px;height:168px;background:linear-gradient(160deg,#b8c4cc,#8fa3b3 60%,#6f8aa3)}
.p-name{position:absolute;top:209px;width:100%;color:var(--accent);font-size:13.5px;font-weight:600}
.p-country{position:absolute;top:229px;width:100%;font-size:10.5px}
.divider{position:absolute;top:253px;left:30px;width:192px;height:1px;background:linear-gradient(90deg,transparent,rgba(255,255,255,.4),transparent)}
.status{position:absolute;top:262px;width:100%;color:var(--accent);font-size:13.5px;font-weight:500}
.hire{position:absolute;top:282px;width:100%;font-size:13.5px;font-weight:500}
.years{position:absolute;top:305px;width:100%;font-size:13px;color:var(--muted)}
.btn{position:absolute;background:var(--btn);color:var(--white);font-weight:600;display:flex;align-items:center;justify-content:center;letter-spacing:.4px}
.btn-profile{left:49px;top:336px;width:154px;height:35px;font-size:11.5px}
.info{left:474px;top:178px;width:525px;height:393px;background:linear-gradient(135deg,rgba(90,24,80,.9),rgba(20,44,120,.9) 55%,rgba(18,30,90,.95))}
.row{position:absolute;left:0;display:flex;align-items:center;height:20px}
.row .label{width:108px;text-align:right;font-size:12px;font-weight:500;letter-spacing:.3px}
.row .colon{width:12px;text-align:center;font-size:12px}
.row .value{margin-left:8px;font-size:12px;font-weight:500}
.row .value.small{font-size:10.5px}
.btn-rehire{left:430px;top:344px;width:77px;height:27px;font-size:10.5px}
.permits{left:201px;top:595px;width:252px;height:352px;background:var(--card-navy)}
.card-title{position:absolute;color:var(--accent);font-size:18px;font-weight:600;letter-spacing:.2px}
.permit{position:absolute;left:21px;display:flex;align-items:center;gap:13px}
.permit svg{width:24px;height:24px;flex:none}
.permit-title{font-size:17.5px;font-weight:600;line-height:1}
.permit-sub{font-size:9.5px;margin-top:2px}
.panel{background:rgba(24,16,56,.92)}
.employee{left:474px;top:595px;width:252px;height:179px}
.company{left:474px;top:794px;width:252px;height:153px}
.arrows{position:absolute;right:12px;top:28px;display:flex;gap:5px}
.inner{position:absolute;left:10px;width:233px;background:#f5f5f5;border-radius:2px;color:var(--ink)}
.avatar{position:absolute;left:8px;top:8px;width:40px;height:38px;background:linear-gradient(160deg,#9aa3a8,#5d666d)}
.emp-name{position:absolute;left:61px;top:14px;font-size:10px;font-weight:600}
.emp-date{position:absolute;left:61px;top:29px;font-size:10px;color:#555}
.blurb{position:absolute;left:8px;font-size:8.5px;line-height:13.5px;color:var(--grey);width:218px}
.co-mark{position:absolute;left:10px;top:8px;width:20px;height:20px;background:#3bb3e0}
.co-name{position:absolute;left:38px;top:8px;font-size:14px;font-weight:600;color:#111;line-height:20px}
.calendar{left:748px;top:595px;width:252px;height:352px;background:var(--white);color:var(--ink)}
.month{position:absolute;top:64px;width:100%;text-align:center;font-size:12px;font-weight:600;letter-spacing:.6px;color:#444}
.cal-line{position:absolute;left:37px;top:94px;width:185px;height:1px;background:#e6e6e6}
.grid{position:absolute;left:30px;top:98px;display:grid;grid-template-columns:repeat(7,28px);column-gap:0;row-gap:0;text-align:center}
.grid span{height:22.5px;line-height:22.5px;font-size:9px}
.grid .wd{color:var(--green);font-size:7.5px;height:24px;line-height:24px}
.grid .off{color:#bbb}
.grid .today{position:relative;color:var(--white)}
.grid .today::before{content:"";position:absolute;left:5px;top:2px;width:18px;height:18px;border-radius:50%;background:#3a8fd6;z-index:0}
.grid .today b{position:relative;font-weight:500}
.note{position:absolute;left:11px;top:245px;width:231px;height:86px;background:#f4f4f4;border:1px solid #e8e8e8}
.note-date{position:absolute;left:13px;top:14px;font-size:9.5px;color:#3a8fd6;font-weight:500}
.footer-line{left:0;top:1017px;width:1200px;height:1px;background:rgba(255,255,255,.15)}
.footer{left:0;top:1057px;width:1200px;text-align:center;font-size:10.5px}
</style>
</head>
<body>
<header class="abs header">
  <div class="abs brand" style="position:absolute">
    <span class="brand-mark"></span>
    <span class="brand-name">SENTINEL GUARD SERVICES, INC.</span>
  </div>
</header>
<nav class="abs nav">
  <span>HOME</span><span>PERSONAL LICNESES</span><span>FORMS\ REQUESTS</span><span>TEAM CONTACTS</span><span>BENEFITS</span><span>TRANING</span><span>EQUIPMENT</span><span>HELP</span>
</nav>

<section class="card profile">
  <div class="photo" role="img" aria-label="Employee portrait photo"></div>
  <div class="p-name">Daniel Whitford</div>
  <div class="p-country">United States</div>
  <div class="divider"></div>
  <div class="status">Status</div>
  <div class="hire">Hire Date 8-1-2016</div>
  <div class="years">17 Years</div>
  <div class="btn btn-profile">VIEW PROFILE</div>
</section>

<section class="card info">
  <div class="row" style="top:36px"><span class="label">NAME</span><span class="colon">:</span><span class="value">Daniel Whitford</span></div>
  <div class="row" style="top:80px"><span class="label">ADDRESS</span><span class="colon">:</span><span class="value small">Lindenweg 42, 10117 Berlin &nbsp;|&nbsp; Germany</span></div>
  <div class="row" style="top:125px"><span class="label">CITY</span><span class="colon">:</span><span class="value">London</span></div>
  <div class="row" style="top:167px"><span class="label">ZIP</span><span class="colon">:</span><span class="value">410352</span></div>
  <div class="row" style="top:213px"><span class="label">PHONE</span><span class="colon">:</span><span class="value">+555-0148392</span></div>
  <div class="row" style="top:255px"><span class="label">CELL PHONE</span><span class="colon">:</span><span class="value">5550172846</span></div>
  <div class="row" style="top:295px"><span class="label">E-MAIL</span><span class="colon">:</span><span class="value">d.whitford@mailbox.test</span></div>
  <div class="btn btn-rehire">RE-HIRE</div>
</section>

<section class="card permits">
  <div class="card-title" style="left:20px;top:26px">Current Permits</div>
  <div class="permit" style="top:74px">
    <svg viewBox="0 0 24 24"><rect x="0" y="4" width="24" height="16" rx="2" fill="var(--yellow)"/><rect x="0" y="8" width="24" height="3" fill="#1c1f55"/><rect x="3" y="14" width="6" height="2" fill="#1c1f55"/></svg>
    <div><div class="permit-title">Guard Card</div><div class="permit-sub">( Red When Invalid )</div></div>
  </div>
  <div class="permit" style="top:148px">
    <svg viewBox="0 0 24 24"><rect x="1" y="3" width="22" height="20" fill="none" stroke="var(--yellow)" stroke-width="2"/><rect x="1" y="3" width="22" height="5" fill="var(--yellow)"/><g fill="var(--yellow)"><rect x="4" y="11" width="3" height="3"/><rect x="9" y="11" width="3" height="3"/><rect x="14" y="11" width="3" height="3"/><rect x="4" y="16" width="3" height="3"/><rect x="9" y="16" width="3" height="3"/><rect x="14" y="16" width="3" height="3"/></g></svg>
    <div><div class="permit-title">Expiring Date</div><div class="permit-sub">( SSN : Late 4 Characters )</div></div>
  </div>
  <div class="permit" style="top:226px">
    <svg viewBox="0 0 24 24"><circle cx="12" cy="12" r="11" fill="var(--yellow)"/><circle cx="12" cy="12" r="7" fill="none" stroke="#1c1f55" stroke-width="1.5"/><circle cx="12" cy="12" r="3.5" fill="none" stroke="#1c1f55" stroke-width="1.5"/></svg>
    <div><div class="permit-title">State ID</div></div>
  </div>
  <div class="permit" style="top:277px">
    <svg viewBox="0 0 24 24"><rect x="0" y="3" width="24" height="18" rx="1" fill="var(--yellow)"/><circle cx="7" cy="10" r="2.5" fill="#1c1f55"/><path d="M3 17c0-3 8-3 8 0z" fill="#1c1f55"/><rect x="13" y="8" width="8" height="2" fill="#1c1f55"/><rect x="13" y="12" width="8" height="2" fill="#1c1f55"/><rect x="13" y="16" width="6" height="2" fill="#1c1f55"/></svg>
    <div><div class="permit-title">Drivers License</div><div class="permit-sub">Expiry Date</div></div>
  </div>
</section>

<section class="card panel employee">
  <div class="card-title" style="left:13px;top:22px">Employee</div>
  <svg class="arrows" width="26" height="12" viewBox="0 0 26 12"><path d="M7 2L3 6l4 4M18 2l4 4-4 4" fill="none" stroke="#fff" stroke-width="1.6"/></svg>
  <div class="inner" style="top:55px;height:108px">
    <div class="avatar" role="img" aria-label="Employee thumbnail photo"></div>
    <div class="emp-name">Daniel Whitford</div>
    <div class="emp-date">September 12 | 2016</div>
    <div class="blurb" style="top:62px">Neque porro quisquam est qui dolorem ipsum quia dolor sit amet, consectetur, adipisci velit...</div>
  </div>
</section>

<section class="card panel company">
  <div class="card-title" style="left:13px;top:12px">Company</div>
  <svg class="arrows" style="top:19px" width="26" height="12" viewBox="0 0 26 12"><path d="M7 2L3 6l4 4M18 2l4 4-4 4" fill="none" stroke="#fff" stroke-width="1.6"/></svg>
  <div class="inner" style="top:46px;height:86px">
    <span class="co-mark"></span>
    <div class="co-name">NORVALE</div>
    <div class="blurb" style="top:44px">Neque porro quisquam est qui dolorem ipsum quia dolor sit amet, consectetur, adipisci velit...</div>
  </div>
</section>

<section class="card calendar">
  <div class="card-title" style="left:16px;top:22px">Calendar</div>
  <div class="month">SEPTEMBER</div>
  <div class="cal-line"></div>
  <div class="grid">
    <span class="wd">SUN</span><span class="wd">MON</span><span class="wd">TUE</span><span class="wd">WED</span><span class="wd">THU</span><span class="wd">FRI</span><span class="wd">SAT</span>
    <span class="off">28</span><span class="off">29</span><span class="off">30</span><span class="off">31</span><span>1</span><span>2</span><span>3</span>
    <span>4</span><span>5</span><span>6</span><span>7</span><span>8</span><span>9</span><span>10</span>
    <span>11</span><span>12</span><span class="today"><b>13</b></span><span>14</span><span>15</span><span>16</span><span>17</span>
    <span>18</span><span>19</span><span>20</span><span>21</span><span>22</span><span>23</span><span>24</span>
    <span>25</span><span>26</span><span>27</span><span>28</span><span>29</span><span>30</span><span class="off">1</span>
  </div>
  <div class="note">
    <div class="note-date">September 13th 2016</div>
    <div class="blurb" style="top:32px;left:12px;width:210px">Neque porro quisquam est qui dolorem ipsum quia dolor sit amet, consectetur, adipisci velit...</div>
  </div>
</section>

<div class="abs footer-line"></div>
<footer class="abs footer">© 2016 Company Name &nbsp;|&nbsp; All Rights Reserved</footer>
</body>
</html>
```